Halvern Guildworks Business Cards
Need out-of-the-box business card design
Halvern Guildworks Business Cards -
Creative Brief
Modern
Peter Strandquell
5172 Orrin St. Denver, CO 80219
peter@halvernguildworks.com
halvernguildworks.com
We exist to foster healthy artist Community, create points of Collaboration and provide tangible benefit to local Causes.

```html
<!DOCTYPE html>
<html lang="en">
<head>
<meta charset="utf-8">
<title>Halvern Guildworks Business Cards</title>
<link href="https://fonts.googleapis.com/css2?family=Crimson+Text:wght@400;600&display=swap" rel="stylesheet">
<style>
  :root {
    --backdrop: #e9e6e1;
    --card: #ffffff;
    --olive: #7d8c2c;
    --gold: #a88a34;
    --ink: #2e2b26;
    --muted: #5a564f;
  }
  * { box-sizing: border-box; margin: 0; padding: 0; }
  html, body { width: 1200px; height: 739px; overflow: hidden; }
  body {
    background: var(--backdrop);
    font-family: "Crimson Text", Georgia, serif;
    color: var(--ink);
    display: flex;
    align-items: center;
    justify-content: center;
    gap: 60px;
  }
  .card {
    position: relative;
    width: 520px;
    height: 297px;
    background: var(--card);
    box-shadow: 0 6px 18px rgba(0,0,0,0.12);
  }
  .brand {
    display: flex;
    align-items: center;
    gap: 12px;
  }
  .brand-dot {
    width: 30px; height: 30px;
    border-radius: 50%;
    background: var(--gold);
  }
  .brand-name {
    font-size: 34px;
    font-weight: 600;
    line-height: 1;
    color: var(--olive);
    letter-spacing: 0.5px;
  }
  /* back side */
  .card-back {
    display: flex;
    flex-direction: column;
    align-items: center;
    justify-content: center;
    gap: 26px;
  }
  .tagline {
    width: 340px;
    text-align: center;
    font-size: 14px;
    line-height: 1.45;
    color: var(--ink);
  }
  /* front side */
  .card-front .brand { position: absolute; left: 34px; top: 62px; }
  .card-front .brand-name { font-size: 30px; }
  .card-front .brand-dot { width: 26px; height: 26px; }
  .holder-name {
    position: absolute;
    right: 34px;
    top: 70px;
    font-size: 17px;
    font-weight: 600;
    color: var(--gold);
  }
  .contact-band {
    position: absolute;
    left: 0;
    top: 168px;
    width: 10px;
    height: 100px;
    background: var(--olive);
  }
  .contact-list {
    position: absolute;
    left: 34px;
    top: 166px;
    list-style: none;
    font-size: 13.5px;
    line-height: 1.55;
    color: var(--muted);
  }
  .contact-list li { display: flex; align-items: center; gap: 8px; }
  .contact-list .address { display: block; padding-left: 0; margin-bottom: 4px; }
  .contact-icon { width: 12px; height: 12px; flex: none; }
</style>
</head>
<body>
  <section class="card card-back">
    <div class="brand">
      <span class="brand-dot"></span>
      <span class="brand-name">halvern guildworks</span>
    </div>
    <p class="tagline">We exist to foster healthy artist Community, create points of Collaboration and provide tangible benefit to local Causes.</p>
  </section>

  <section class="card card-front">
    <div class="brand">
      <span class="brand-dot"></span>
      <span class="brand-name">halvern guildworks</span>
    </div>
    <p class="holder-name">Peter Strandquell</p>
    <span class="contact-band"></span>
    <ul class="contact-list">
      <li class="address">5172 Orrin St.<br>Denver, CO 80219</li>
      <li>
        <svg class="contact-icon" viewBox="0 0 12 12"><path d="M2.5 1h2l1 2.5-1.3 1a6 6 0 0 0 3.3 3.3l1-1.3L11 7.5v2A1.5 1.5 0 0 1 9.5 11 8.5 8.5 0 0 1 1 2.5 1.5 1.5 0 0 1 2.5 1z" fill="#a88a34"/></svg>
        3035550148
      </li>
      <li>
        <svg class="contact-icon" viewBox="0 0 12 12"><rect x="1" y="2.5" width="10" height="7" rx="1" fill="none" stroke="#7d8c2c" stroke-width="1.2"/><path d="M1.5 3l4.5 3.5L10.5 3" fill="none" stroke="#7d8c2c" stroke-width="1.2"/></svg>
        rtolvessan@halvernguildworks.com
      </li>
      <li>
        <svg class="contact-icon" viewBox="0 0 12 12"><circle cx="6" cy="6" r="4.8" fill="none" stroke="#a88a34" stroke-width="1.2"/><path d="M1.2 6h9.6M6 1.2c-2.4 2.6-2.4 7 0 9.6M6 1.2c2.4 2.6 2.4 7 0 9.6" fill="none" stroke="#a88a34" stroke-width="1"/></svg>
        www.halvernguildworks.com
      </li>
    </ul>
  </section>
</body>
</html>
```